Health Clinic treating people with mental illness needs a website

We need a website for a new mental health clinic based in Florida called Tidewell Balance USA. We treat people with mental health issues such as depression, PTSD, Bipolar, chronic pain, etc. I want the website to be easy to follow and inviting to the visitors. It should be easy to locate the different treatment options and how to go about contacting and making appointments. The images on the website should be something that the patients can relate to, whether a close up of a woman's face, something that conveys emotion. The patients visiting this website are often sad and miserable, they need to be able to feel comfortable when they look at this website. I want them to feel that we understand where they are coming from. I like colors such as purple, turquoise, lavender.

Target Market(s)

College students, veterans, anyone with mental illness

Industry/Entity Type

Health And Wellness

Font styles to use
Serif
Sans Serif

Colors

Designer to choose colors to be used in the design.

Requirements
Must have
• There should be a home/landing page, about us page, treatment page, contact page, and a FAQ page. I've included my logo below.
Nice to have
• The flow of the web pages should be calming and welcoming. I want people to feel warm and understood when they enter our page.
Should not have
• The images and writing should not be overly stimulating or aggressive.

```html
<!DOCTYPE html>
<html lang="en">
<head>
<meta charset="utf-8">
<title>Tidewell Balance USA – Mental Health Clinic</title>
<link href="https://fonts.googleapis.com/css2?family=IBM+Plex+Sans:wght@400;500;600;700&display=swap" rel="stylesheet">
<style>
:root{
  --purple:#7d1f82;
  --purple-btn:#a04a9b;
  --teal:#2aa98d;
  --ink:#2b2b2b;
  --muted:#4a4a4a;
  --blush:#f4f0f0;
  --line:#d9d4d4;
  --white:#ffffff;
}
*{box-sizing:border-box;margin:0;padding:0}
html,body{width:1200px;height:4505px;overflow:hidden}
body{font-family:"IBM Plex Sans",Arial,sans-serif;color:var(--ink);background:var(--white);position:relative}
section,header,footer{position:absolute;left:0;width:1200px}
.abs{position:absolute}
.photo{position:absolute}

/* header */
.site-header{top:0;height:100px;background:var(--white)}
.brand{left:131px;top:37px;display:flex;align-items:center;gap:8px;font-size:19px;font-weight:600;color:var(--purple);white-space:nowrap}
.brand-dot{width:12px;height:12px;border-radius:50%;background:var(--teal);flex:none}
.main-nav{left:388px;top:43px;display:flex;gap:34px;font-size:14px;font-weight:600;letter-spacing:.3px;white-space:nowrap}
.main-nav a{color:var(--ink);text-decoration:none}
.main-nav a.active{color:var(--purple);text-decoration:underline;text-underline-offset:4px}
.social{left:973px;top:37px;display:flex;gap:9px}
.social span{width:26px;height:26px;border-radius:50%;background:#3f5fb0}
.social span:nth-child(2){background:#1da1f2}
.social span:nth-child(3){background:#1b1b3a}

/* hero */
.hero{top:100px;height:530px}
.hero .photo{inset:0;background:linear-gradient(180deg,#e8dcc0 0%,#d8c08f 45%,#b98a3c 75%,#8d6526 100%)}
.hero-title{left:782px;top:108px;font-size:61px;line-height:66px;font-weight:700;color:var(--purple);letter-spacing:1px}
.btn{display:flex;align-items:center;justify-content:center;color:var(--white);font-weight:600;letter-spacing:.5px;background:var(--teal);white-space:nowrap}
.hero .btn{left:785px;top:330px;width:271px;height:61px;font-size:19px}

/* welcome */
.welcome{top:630px;height:577px;background:var(--blush)}
.welcome .photo{left:75px;top:49px;width:544px;height:477px;background:linear-gradient(135deg,#d9d4cf,#a9b4c4 50%,#e6d9d2)}
.welcome-kicker{left:669px;top:86px;font-size:23px;font-weight:600;color:var(--ink)}
.welcome-title{left:667px;top:120px;font-size:37px;font-weight:600;color:var(--ink);letter-spacing:.5px;white-space:nowrap}
.welcome-copy{left:670px;top:200px;width:385px;font-size:15px;line-height:22.5px;color:var(--muted)}
.welcome-copy p+p{margin-top:32px}

/* why */
.why{top:1207px;height:143px;text-align:center}
.section-title{width:100%;font-size:24px;font-weight:600;color:var(--ink);letter-spacing:.5px;text-align:center}
.why .section-title{top:50px}
.why-sub{top:90px;width:100%;font-size:15px;color:var(--muted)}

/* band */
.band{top:1350px;height:527px}
.band .photo{inset:0;background:linear-gradient(180deg,#55482f 0%,#8b7a5d 35%,#6d5e4a 65%,#3b3230 100%)}
.benefit-card{left:201px;top:75px;width:798px;height:377px;background:var(--white);box-shadow:0 2px 10px rgba(0,0,0,.2)}
.benefit-grid{position:absolute;left:30px;top:30px;width:747px;height:322px;border:1.5px solid #555}
.cell{position:absolute;padding:22px 24px;border-color:#555;border-style:solid;border-width:0}
.cell h3{font-size:13.5px;font-weight:700;letter-spacing:.3px;margin-bottom:8px}
.cell p{font-size:12.5px;line-height:17.5px;color:var(--muted)}
.row1{top:0;height:130px;border-bottom-width:1.5px}
.row2{top:130px;height:190px}

/* treatment */
.treatment{top:1877px;height:930px;background:var(--blush)}
.treatment .section-title{top:53px}
.treat-card{position:absolute;width:298px;height:317px;background:var(--white);box-shadow:0 1px 4px rgba(0,0,0,.08)}
.treat-card .photo{left:0;top:0;width:298px;height:245px}
.treat-card h3{position:absolute;left:26px;top:264px;font-size:16px;font-weight:700;letter-spacing:.5px}
.treatment .btn{left:486px;top:830px;width:226px;height:48px;font-size:14px}

/* testimonials */
.testimonials{top:2807px;height:465px}
.testimonials .section-title{top:60px}
.quote-mark{font-size:64px;font-weight:700;color:var(--purple-btn);line-height:1}
.quote-text{left:305px;top:145px;width:590px;text-align:center;font-size:21px;line-height:31px;color:var(--ink)}
.author{top:328px;width:100%;text-align:center;font-size:16px;font-weight:700;letter-spacing:.5px}
.dots{left:582px;top:394px;display:flex;gap:8px}
.dots span{width:5px;height:5px;border-radius:50%;background:#444}
.dots span.on{background:none;border:1px solid #444}

/* contact */
.contact{top:3272px;height:716px;background:var(--blush)}
.contact .section-title.first{top:57px}
.field{position:absolute;background:var(--white);border:1px solid #c8c3c3;font-size:12.5px;color:#444;padding:15px 16px;letter-spacing:.3px}
.submit{left:530px;top:403px;width:140px;height:44px;background:var(--purple-btn);font-size:18px}
.contact .section-title.second{top:522px}
.info-rule{left:129px;top:597px;width:940px;height:1px;background:var(--line)}
.info-div{top:597px;width:1px;height:74px;background:var(--line)}
.info{top:622px;font-size:17px;line-height:26px;color:var(--ink);white-space:nowrap}

/* map */
.map{top:3988px;height:437px}
.map .photo{inset:0;background:linear-gradient(90deg,#e4e2de 0%,#eceae6 60%,#d6e8d0 75%,#cfe2ee 100%)}
.pin{left:574px;top:190px}

/* footer */
.site-footer{top:4425px;height:80px;text-align:center;font-size:13px;color:var(--ink);padding-top:36px}
</style>
</head>
<body>

<header class="site-header">
  <div class="abs brand"><span>Tidewell Balance USA</span><span class="brand-dot"></span></div>
  <nav class="abs main-nav">
    <a class="active" href="#">HOME</a><a href="#">ABOUT US</a><a href="#">TREATMENT</a><a href="#">FAQ</a><a href="#">CONTACT US</a>
  </nav>
  <div class="abs social" aria-label="Social links"><span></span><span></span><span></span></div>
</header>

<section class="hero">
  <div class="photo" role="img" aria-label="Woman with open arms enjoying warm sunlight in a golden meadow"></div>
  <h1 class="abs hero-title">MENTAL<br>HEALTH<br>CLINIC</h1>
  <a class="abs btn">BOOK AN APPOINTMENT</a>
</section>

<section class="welcome">
  <div class="photo" role="img" aria-label="Thoughtful woman talking with a counsellor in a bright room"></div>
  <div class="abs welcome-kicker">WELCOME TO</div>
  <h2 class="abs welcome-title">TIDEWELL BALANCE</h2>
  <div class="abs welcome-copy">
    <p>Lorem ipsum dolor sit amet, consectetur adipiscing elit, sed do eiusmod tempor incididunt ut labore et dolore magna aliqua. Ut enim ad minim veniam, quis nostrud exercitation ullamco laboris nisi ut aliquip ex ea commodo consequat. Duis aute irure dolor in reprehenderit in voluptate.</p>
    <p>Duis aute irure dolor in reprehenderit in voluptate velit esse cillum dolore eu fugiat nulla pariatur error sit voluptatem accusantium doloremque laudantium, totam rem aperiam, eaque ipsa quae ab illo inventore veritatis</p>
  </div>
</section>

<section class="why">
  <h2 class="abs section-title">WHY CHOOSE US</h2>
  <div class="abs why-sub">Lorem ipsum dolor</div>
</section>

<section class="band">
  <div class="photo" role="img" aria-label="Soft evening landscape with hills and trees"></div>
  <div class="abs benefit-card">
    <div class="benefit-grid">
      <div class="cell row1" style="left:0;width:287px;border-right-width:1.5px"><h3>SUPPORT</h3><p>Duis aute irure dolor in repreh enderit in voluptate velit esse cillum dolore eu fugiat nulla pariatur.</p></div>
      <div class="cell row1" style="left:287px;width:257px;border-right-width:1.5px"><h3>SATISFACTION</h3><p>Duis aute irure dolor in repreh enderit in voluptate velit esse cillum dolore eu fugiat nulla pariatur.</p></div>
      <div class="cell row1" style="left:544px;width:201px"><h3>BETTER HEALTH</h3><p>Duis aute irure dolor in repreh enderit in volup tate velit esse.</p></div>
      <div class="cell row2" style="left:0;width:381px;border-right-width:1.5px"><h3>LOREM IPSUM</h3><p>Duis aute irure dolor in repreh enderit in voluptate velit esse cillum dolore eu fugiat nulla pariatur. expound the actual teachings of the great explorer of the truth, the master-builder of human happiness. No one rejects, dislikes, or avoids pleasure itself</p></div>
      <div class="cell row2" style="left:381px;width:163px;border-right-width:1.5px"><h3>LOREM IPSUM</h3><p>Duis aute irure dolor in repreh enderit in volup tate velit esse.</p></div>
      <div class="cell row2" style="left:544px;width:201px"><h3>LOREM IPSUM</h3><p>Duis aute irure dolor in repreh enderit in volup tate velit esse.</p></div>
    </div>
  </div>
</section>

<section class="treatment">
  <h2 class="abs section-title">OUR TREATMENT</h2>
  <div class="treat-card" style="left:136px;top:134px"><div class="photo" role="img" aria-label="Woman sitting alone on a sofa looking downcast" style="background:linear-gradient(135deg,#6d5a52,#3e302c)"></div><h3>DEPRESSION</h3></div>
  <div class="treat-card" style="left:451px;top:134px"><div class="photo" role="img" aria-label="Black and white image of a distressed person holding their head" style="background:linear-gradient(135deg,#4a4a4a,#1d1d1d)"></div><h3>PTSD</h3></div>
  <div class="treat-card" style="left:764px;top:134px"><div class="photo" role="img" aria-label="Man sitting against a pale wall with hands on his head" style="background:linear-gradient(135deg,#c8d3dc,#8d9ba8)"></div><h3>BIPOLAR</h3></div>
  <div class="treat-card" style="left:136px;top:472px"><div class="photo" role="img" aria-label="Person holding a painful wrist" style="background:linear-gradient(135deg,#5d7072,#2f3a3d)"></div><h3>CHRONIC PAIN</h3></div>
  <div class="treat-card" style="left:451px;top:472px"><div class="photo" role="img" aria-label="Woman with open arms at a golden sunset" style="background:linear-gradient(180deg,#f0b948,#c8741c)"></div><h3>MINDFULNESS</h3></div>
  <div class="treat-card" style="left:764px;top:472px"><div class="photo" role="img" aria-label="Smiling woman in a cosy sweater holding a mug" style="background:linear-gradient(135deg,#dfe6ea,#b3a59a)"></div><h3>ANXIETY</h3></div>
  <a class="abs btn">BOOK AN APPOINTMENT</a>
</section>

<section class="testimonials">
  <h2 class="abs section-title">TESTIMONIALS</h2>
  <div class="abs quote-mark" style="left:259px;top:118px">&ldquo;</div>
  <p class="abs quote-text">Duis aute irure dolor in repreh enderit in voluptate velit esse cillum dolore eu fugiat nulla pariatur. expound the actual teachings of the great explorer of the truth, the master builder of human happiness. No one rejects dislikes or avoids pleasure itself</p>
  <div class="abs quote-mark" style="left:765px;top:280px">&rdquo;</div>
  <div class="abs author">DANIEL</div>
  <div class="abs dots"><span></span><span class="on"></span><span></span></div>
</section>

<section class="contact">
  <h2 class="abs section-title first">YOUR HEALTH STARTS HERE</h2>
  <div class="field" style="left:229px;top:133px;width:352px;height:48px">NAME</div>
  <div class="field" style="left:595px;top:133px;width:353px;height:48px">E MAIL</div>
  <div class="field" style="left:229px;top:194px;width:719px;height:174px">MESSAGE</div>
  <a class="abs btn submit">SUBMIT</a>
  <h2 class="abs section-title second">CONTACT US</h2>
  <div class="abs info-rule"></div>
  <div class="abs info-div" style="left:324px"></div>
  <div class="abs info-div" style="left:637px"></div>
  <div class="abs info" style="left:130px">Phone<br>123 - 456 - 7890</div>
  <div class="abs info" style="left:376px">Email<br>info@tidewellbalance.com</div>
  <div class="abs info" style="left:677px">Address<br>220 Harbor Light Avenue Tampa, FL 33602</div>
</section>

<section class="map">
  <div class="photo" role="img" aria-label="Street map showing the clinic location"></div>
  <svg class="abs pin" width="24" height="34" viewBox="0 0 24 34" aria-hidden="true">
    <path d="M12 0C5.4 0 0 5.3 0 11.8 0 20.6 12 34 12 34s12-13.4 12-22.2C24 5.3 18.6 0 12 0z" fill="#d93a2b"/>
    <circle cx="12" cy="11.5" r="4.5" fill="#8f1f15"/>
  </svg>
</section>

<footer class="site-footer">Copyright © 2019 All Rights Reserved</footer>

</body>
</html>
```